Nine Petals - `Brochure Design Project

We have created a range of Natural & Organic Skincare that we plan on selling to the tourists that visit Australia.

We need a DL sized brochure with approx. 8 x pages designed to reflect a high end Natural & Organic skincare range.

The brand is called 'Quiet Meadow' and the range is called 'Nine Petals'.

The point of difference with our competitors is that each product contains six unique Australian botanicals that have been chosen for their benefits to the skin. I will attach the first draft copy that was written for each product and appears on the packaging.

We also need to make space for a paragraph or two on the background or philosophy behind the ‘Nine Petals’ brand. Why we chose these ingredients, why it is important to use natural & organic ingredients that don’t contain the harmful parabens etc.. The design should have images that refer to that fact that the product is uniquely Australian, natural & organic and should draw on the benefits that Australia is perceived as a ‘pure’, ‘clean’ and ‘natural’ environment.

I have also attached the product artwork for your reference – please note that the gold colour is gold foil. We have samples of the printed boxes and they look great. We do not have product photo's yet and will need positionals from you before we do.

We have the following products in the range. All (except the Lip Balm) contain the six Australian botanicals.

1. Lanolin Lip Balm
2. Lanolin Body Cream
3. Lanolin day cream
4. Placenta (plant) Cream
5. Placenta (plant) Serum
6. Collagen Cream
7. Collagen Serum

The featured products are the Placenta and Collagen products. The lanolin products are secondary.

We do not have images of the Lanolin Body cream or Lip balm. Please simply create positionals.

Please let me know if there is anything else you require.

Reason: I am currently away and will be returning to the office on 10th October. Thank you.

Target Market(s)

Customers are paying a premium so the design must reflect this.

Customers that like Natural & Organic products.

We have included gold foil in the packaging to reflect a high end product. We have also included gold foil as a large part of our target marget is Asian, in particula Chinese. In saying this, the design needs to appeal to both Western and Asian customers.

Industry/Entity Type

Environment

Requirements
Nice to have
• Nature images
Beautiful lady images
Lifestyle images

The design should include the above features but at the same time reflect a classy, high end range.

```html
<!DOCTYPE html>
<html lang="en">
<head>
<meta charset="utf-8">
<title>Quiet Meadow – Botanical Ingredients</title>
<link rel="stylesheet" href="https://fonts.googleapis.com/css2?family=Didact+Gothic&family=Noto+Serif:ital,wght@1,700&display=swap">
<style>
  :root {
    --paper: #e9e7d7;
    --green: #16553a;
    --gold: #e0bf2b;
    --gold-soft: #f1d98a;
    --white: #ffffff;
  }
  * { box-sizing: border-box; margin: 0; padding: 0; }
  html, body { width: 1200px; height: 1200px; overflow: hidden; background: var(--paper); }
  .page {
    position: relative; width: 1200px; height: 1200px;
    background: var(--paper); overflow: hidden;
    font-family: "Didact Gothic", "Century Gothic", sans-serif; color: var(--green);
  }
  .mimosa-top {
    position: absolute; left: 180px; top: 10px; width: 540px; height: 330px;
    background: radial-gradient(ellipse at 60% 35%, #f0b323 0%, #f5cb4a 35%, rgba(233,231,215,0) 72%);
  }
  .wattle-bottom {
    position: absolute; left: 420px; top: 670px; width: 260px; height: 440px;
    background: radial-gradient(ellipse at 50% 50%, rgba(245,225,130,.75) 0%, rgba(245,225,130,.35) 45%, rgba(233,231,215,0) 75%);
  }
  .headline { position: absolute; left: 100px; top: 270px; display: flex; align-items: center; }
  .headline-number {
    font-size: 190px; line-height: 1; color: var(--gold); font-weight: 400; margin-right: 8px;
  }
  .headline-words { font-size: 37px; line-height: 1.05; letter-spacing: 2px; color: var(--green); }
  .ingredient { position: absolute; width: 140px; }
  .ingredient-ring {
    position: absolute; width: 110px; height: 110px; border-radius: 50%;
    background: var(--white);
    display: flex; align-items: center; justify-content: center;
  }
  .ingredient-photo { width: 92px; height: 92px; border-radius: 50%; }
  .ingredient-label {
    position: absolute; font-family: "Noto Serif", Georgia, serif; font-style: italic; font-weight: 700;
    font-size: 23px; line-height: 24px; color: var(--green); white-space: nowrap;
  }
  .maker { position: absolute; left: 100px; top: 876px; font-size: 18px; line-height: 23px; letter-spacing: 1.6px; }
  .details { position: absolute; left: 660px; width: 500px; }
  .details h2 {
    font-family: "Noto Serif", Georgia, serif; font-style: italic; font-weight: 700;
    font-size: 22.5px; line-height: 28px; color: var(--green);
  }
  .details p { font-size: 19.5px; line-height: 23px; color: var(--green); margin-top: 2px; }
  .footer-band {
    position: absolute; left: 0; top: 1112px; width: 1200px; height: 88px; background: var(--gold);
    color: var(--white); font-size: 23px; letter-spacing: .6px;
  }
  .footer-band span { position: absolute; top: 30px; }
</style>
</head>
<body>
<main class="page">
  <div class="mimosa-top" role="img" aria-label="Sprig of golden wattle blossom"></div>
  <div class="wattle-bottom" role="img" aria-label="Faint branch of pale yellow wattle flowers"></div>

  <div class="headline">
    <span class="headline-number">6</span>
    <span class="headline-words">BOTANICAL<br>INGREDIENTS</span>
  </div>

  <div class="ingredient-ring" style="left:99px;top:445px"><div class="ingredient-photo" role="img" aria-label="Red rosehips" style="background:radial-gradient(circle,#e8323a,#b81f2b)"></div></div>
  <div class="ingredient-ring" style="left:242px;top:445px"><div class="ingredient-photo" role="img" aria-label="Halved avocado" style="background:radial-gradient(circle,#cfd98a,#3f6a2a)"></div></div>
  <div class="ingredient-ring" style="left:388px;top:445px"><div class="ingredient-photo" role="img" aria-label="Green Kakadu plums" style="background:radial-gradient(circle,#b9d274,#7da640)"></div></div>
  <div class="ingredient-ring" style="left:99px;top:627px"><div class="ingredient-photo" role="img" aria-label="Wheat ears" style="background:radial-gradient(circle,#e8c77a,#f4f1e6)"></div></div>
  <div class="ingredient-ring" style="left:242px;top:627px"><div class="ingredient-photo" role="img" aria-label="Dark blue Davidson plums" style="background:radial-gradient(circle,#4a5fa0,#1f2a55)"></div></div>
  <div class="ingredient-ring" style="left:388px;top:627px"><div class="ingredient-photo" role="img" aria-label="Red rosella flower bud" style="background:radial-gradient(circle,#b02a30 0%,#d04048 30%,#f6f3ea 60%)"></div></div>

  <span class="ingredient-label" style="left:89px;top:570px">ORGANIC<br>Rosehip Oil</span>
  <span class="ingredient-label" style="left:250px;top:570px">ORGANIC<br>Avocado</span>
  <span class="ingredient-label" style="left:406px;top:570px">Kakadu<br>Plum</span>
  <span class="ingredient-label" style="left:97px;top:758px">Vitamin E</span>
  <span class="ingredient-label" style="left:248px;top:758px">Davidson<br>Plum</span>
  <span class="ingredient-label" style="left:406px;top:758px">Rosella</span>

  <div class="maker">
    Manufactured for:<br>
    Evergrove Wellness Pty. Ltd.<br>
    4/58b Harbour View Lane,<br>
    Seaforth&nbsp; NSW&nbsp; 2092 Australia<br>
    www.quietmeadow.com.au
  </div>

  <section class="details" style="top:184px">
    <h2>ORGANIC Rosehip Oil</h2>
    <p>rich in Vitamin E &amp; Omega 3, 6 and 9 essential fatty acids. Your skin will be comforted, deeply moisturised, look vibrant, feeling smooth and soft.</p>
  </section>
  <section class="details" style="top:322px">
    <h2>ORGANIC Avocado</h2>
    <p>provides a rich source of Vitamin A, B, D and E. It penetrates the skin evenly and quickly, allowing skin to be smooth and moisturised.</p>
  </section>
  <section class="details" style="top:440px">
    <h2>Kakadu Plum</h2>
    <p>one of the world’s richest sources of Vitamin C. The plant is found in Northern Australia. It is used most commonly in skincare to brighten and plump the skin, giving it a youthful appearance.</p>
  </section>
  <section class="details" style="top:607px">
    <h2>Vitamin E</h2>
    <p>a strong anti-oxidant vital in protecting skin cells from UV light, pollution and other elements that can damage the skin. It helps improves overall skin health by deeply penetrating the skin to reduce the appearance of deep wrinkles, dry and cracked skin.</p>
  </section>
  <section class="details" style="top:796px">
    <h2>Davidson Plum</h2>
    <p>a native Australian fruit found in the rainforests of Queensland. It contains high levels of anti-oxidants. This provides significant hydration for the skin and strengthens elasticity.</p>
  </section>
  <section class="details" style="top:944px">
    <h2>Rosella Extract</h2>
    <p>a native species of hibiscus and high in anti-oxidants. It stimulates a natural, healthy metabolism for optimal skin cell renewal.</p>
  </section>

  <footer class="footer-band">
    <span style="left:136px">Natural Australian Skincare</span>
    <span style="left:728px">www.quietmeadow.com.au</span>
  </footer>
</main>
</body>
</html>
```